!! We Need YOU !! Las Vegas !! Pool Cleaning Company looking for a Brochure Design!

We are a pool/spa/water feature cleaning company for commercial properties. We are looking for a professional looking brochure to hand to clients as we speak to them about our business. We would like something that stays away from back yard pool themes like pool toys and diving boards. Our properties are resorts, hotels, casinos, and private estates so we need something to grab their attention!

Our company name is "Premier Basin Stewards"
Our slogan is "Sparkling Results"
Phone is 702-555-0187
email is rkelvane@basinstewardsgroup.com
webpage www.premier-basin-stewardsgrp.com
(I know those are long! Sorry!)

We DO NOT need to include all of this in one brochure but here are some ideas for wording:

Swimming pools are a way of life in Las Vegas and PBS loves being a part of that culture. PBS is a company that has a team with 15 years of experience that spans across the Las Vegas Valley working on commercial properties. We understand the complexity of managing commercial pools and bring our resources and experience to provide you with a service that can not be matched.

the PBS advantage:
Since 2002 our team has had the privilege of providing services to resorts, casinos, hotels, and private estates. The tried and true business practices of our team have been tested and refined over the years. These practices have resulted in a set of standards to ensure PBS is a company of distinction. We believe our commitment to safety, integrity, affordability, and professionalism help us deliver the best possible pool cleaning services in Las Vegas.

Safety: PBS understands the specific requirements of the health department and chemical regulations. We work closely with the health department and exceed their requirements to help keep your property safe and compliant. PBS has developed a set of systems and programs that have been proven within the industry to accomplish reliance to safety. Our employees are dedicated to using the most advanced tools, training, and technology available to keep your property clean and safe.
Integrity:
You are secure with PBS. We pride ourselves on providing our customers with the right care for your property through honest and straightforward service. PBS will adhere to quality and honesty. PBS will have an active regard for our standards of conduct. It is our sincere belief that by establishing relationships through responsiveness to the customer's needs and dedication to our customers, that we will become the standard by which all other companies will measure their success.

Affordability: You can be assured that PBS will provide professional services at a reasonable rate. PBS will establish a long-term and beneficial relationship while fixing your costs for the next 1-5 years. We strive to keep our focus on commercial properties which means our focus is on your property. We offer exceptional pricing on cleaning, maintenance, and repair services.
Professionalism:
With any industry, you have a spectrum of professionalism. PBS strives to be at the top of that spectrum by encompassing all of the aforementioned qualities, plus many more. We strive to be the leader in providing quality service through education and certification. PBS employees always show respect for you and your property and are highly knowledgeable, courteous, and efficient. PBS will exceed expectations in the areas of accountability, customer support, and expertise.

We will be proactive rather than reactive to potentially problematic areas with proper advance planning.

When you work with PBS you can trust that our experience in the hospitality industry brings unlimited service, quick response, and a reputation to serve. If you have a commercial pool in the Las Vegas area, you should have our number.
If you are looking for knowledgeable and dependable pool cleaning and maintenance in Las Vegas, look no further than PBS.

Maintenance
▪ Regular Maintenance Services
▪ Weekly Pool/Spa Service
▪ One Time Clean-Ups
▪ DE Filter Cleaning
▪ Drain Pool & Refill
▪ Impellers
▪ Valves
▪ Algae Removal
▪ Back Wash
▪ Water Testing & Balancing
▪ Equipment Inspection
▪ Skimming, Brushing, & Leafing
Emergency service 24 hours per day, 7 days per week
Updates

Target Market(s)

High-end Resorts and properties.

Industry/Entity Type

It Company

Font styles to use
Serif
Sans Serif

Requirements
Must have
• Professional look and feel.
• Size/shape will depend on design concept-I do not care if it is traditional fold or something creative.
• Needs to have a front and back complete concept.
Nice to have
• I would like to see some ideas using our font and colors.
• I would like to focus on pictures with no buildings or beaches in them.
Should not have
• No pool toys, diving boards, palm trees, beach, or anything with a "backyard" pool feel.

```html
<!DOCTYPE html>
<html lang="en">
<head>
<meta charset="utf-8">
<title>Premier Basin Stewards – Brochure</title>
<link rel="stylesheet" href="https://fonts.googleapis.com/css2?family=Quicksand:wght@600;700&family=Open+Sans:wght@300;400;700&display=swap">
<style>
  :root {
    --page: #e6e8ea;
    --sky: #5cc1ec;
    --sky-light: #8fd4f2;
    --azure: #2a8fd0;
    --deep: #1357a6;
    --navy: #0d3f86;
    --slate: #6a6c6f;
    --white: #ffffff;
    --logo-blue: #2e86c9;
  }
  * { box-sizing: border-box; margin: 0; padding: 0; }
  html, body { width: 1200px; height: 880px; overflow: hidden; }
  body {
    background: var(--page);
    font-family: "Open Sans", Arial, sans-serif;
    position: relative;
  }
  .brochure {
    position: absolute;
    left: 170px; top: 90px;
    width: 860px; height: 700px;
    display: flex;
    box-shadow: 0 6px 24px rgba(0,0,0,0.12);
  }
  .panel { position: relative; height: 100%; overflow: hidden; }

  /* Services panel */
  .panel-services { width: 340px; background: var(--sky); color: var(--white); }
  .services-heading {
    position: absolute; left: 40px; top: 44px;
    font-family: "Quicksand", Arial, sans-serif; font-weight: 700;
    font-size: 28px; letter-spacing: 0.3px;
  }
  .services-heading-rule {
    position: absolute; left: 230px; top: 68px; width: 110px; height: 1px;
    background: rgba(255,255,255,0.7);
  }
  .services-list {
    position: absolute; left: 40px; top: 104px;
    list-style: none; font-weight: 300; font-size: 14.5px; line-height: 21.6px;
  }
  .emergency-note {
    position: absolute; left: 44px; top: 386px; width: 284px;
    font-weight: 300; font-size: 14px; line-height: 20px;
  }
  .services-art { position: absolute; left: 0; top: 0; }

  /* Contact flap */
  .panel-contact { width: 140px; background: var(--sky); }
  .contact-art { position: absolute; left: 0; top: 0; }
  .contact-logo {
    position: absolute; left: 38px; top: 220px;
    writing-mode: vertical-rl;
    display: flex; align-items: center; gap: 6px;
    font-family: "Open Sans", Arial, sans-serif; font-weight: 700;
    font-size: 30px; color: var(--white);
  }
  .contact-logo .mark { width: 14px; height: 14px; border-radius: 50%; background: var(--white); }
  .contact-label {
    position: absolute; left: 64px; top: 360px;
    writing-mode: vertical-rl; font-size: 10px; color: var(--white);
  }
  .contact-icon { position: absolute; left: 50px; top: 416px; }
  .contact-phone {
    position: absolute; left: 28px; top: 460px;
    writing-mode: vertical-rl; font-size: 22px; color: var(--white); letter-spacing: 1px;
  }
  .contact-email {
    position: absolute; left: 66px; top: 456px;
    writing-mode: vertical-rl; font-size: 9.5px; line-height: 12px; color: var(--white);
    width: 26px; height: 200px;
  }

  /* Cover */
  .panel-cover { width: 380px; background: var(--white); }
  .cover-art { position: absolute; left: 0; top: 0; }
  .cover-logo {
    position: absolute; left: 76px; top: 82px;
    display: flex; align-items: center; gap: 12px;
    color: var(--logo-blue); font-weight: 700;
  }
  .cover-logo .mark { width: 40px; height: 40px; border-radius: 50%; background: var(--logo-blue); }
  .cover-logo .name { font-size: 52px; line-height: 1; letter-spacing: 1px; }
  .cover-logo-sub {
    position: absolute; left: 128px; top: 140px;
    font-size: 10px; font-weight: 700; color: var(--logo-blue); letter-spacing: 0.8px; text-transform: uppercase;
  }
  .cover-title {
    position: absolute; right: 22px; top: 556px; text-align: right;
    color: var(--white); font-weight: 400; font-size: 28px; line-height: 36px;
    text-shadow: 0 1px 3px rgba(0,0,0,0.35);
  }
  .cover-slogan {
    position: absolute; right: 22px; top: 634px;
    color: var(--white); font-weight: 700; font-size: 16px;
  }
  .cover-url {
    position: absolute; right: 22px; top: 676px;
    color: var(--white); font-size: 9.5px;
  }
</style>
</head>
<body>
<main class="brochure">

  <section class="panel panel-services">
    <svg class="services-art" width="340" height="700" viewBox="0 0 340 700">
      <path d="M0 700 L0 470 Q150 425 300 485 Q340 540 340 580 L340 700 Z" fill="var(--azure)"/>
      <circle cx="140" cy="592" r="140" fill="var(--deep)"/>
      <circle cx="140" cy="592" r="129" fill="var(--sky-light)"/>
      <defs>
        <radialGradient id="spaTones" cx="45%" cy="40%" r="70%">
          <stop offset="0" stop-color="#d9dcd4"/>
          <stop offset="0.45" stop-color="#6f8a4a"/>
          <stop offset="1" stop-color="#2a3326"/>
        </radialGradient>
      </defs>
      <circle cx="140" cy="592" r="120" fill="url(#spaTones)" role="img" aria-label="Spa still life photo: white orchid, bamboo stalks, rolled green towel and candle"/>
    </svg>
    <h2 class="services-heading">Maintenance</h2>
    <span class="services-heading-rule"></span>
    <ul class="services-list">
      <li>Regular Maintenance Services</li>
      <li>Weekly Pool/Spa Service</li>
      <li>One Time Clean-Ups</li>
      <li>DE Filter Cleaning</li>
      <li>Drain Pool &amp; Refill</li>
      <li>Impellers</li>
      <li>Valves</li>
      <li>Algae Removal</li>
      <li>Back Wash</li>
      <li>Water Testing &amp; Balancing</li>
      <li>Equipment Inspection</li>
      <li>Skimming, Brushing, &amp; Leafing</li>
    </ul>
    <p class="emergency-note">Emergency service 24 hours per day, 7 days per week</p>
  </section>

  <aside class="panel panel-contact">
    <svg class="contact-art" width="140" height="700" viewBox="0 0 140 700">
      <rect x="0" y="0" width="140" height="700" fill="var(--sky)"/>
      <rect x="0" y="0" width="6" height="700" fill="rgba(255,255,255,0.35)"/>
      <ellipse cx="170" cy="420" rx="160" ry="280" fill="var(--slate)"/>
    </svg>
    <div class="contact-logo"><span class="mark"></span><span>PBS</span></div>
    <span class="contact-label">Call us:</span>
    <svg class="contact-icon" width="34" height="34" viewBox="0 0 34 34">
      <circle cx="17" cy="17" r="15" fill="none" stroke="var(--white)" stroke-width="2"/>
      <path d="M11 10 q-2 2 0 6 q3 6 8 8 q4 1 5-1 l-3-3 q-1 1-2 0 q-3-2-4-5 q0-1 1-2 z" fill="var(--white)"/>
    </svg>
    <span class="contact-phone">702-555-0187</span>
    <span class="contact-email">rkelvane@basinstewardsgroup.com</span>
  </aside>

  <section class="panel panel-cover">
    <svg class="cover-art" width="380" height="700" viewBox="0 0 380 700">
      <defs>
        <linearGradient id="poolTones" x1="0" y1="0" x2="0" y2="1">
          <stop offset="0" stop-color="#ffffff"/>
          <stop offset="0.2" stop-color="#c7cbd0"/>
          <stop offset="0.42" stop-color="#8a7a66"/>
          <stop offset="0.62" stop-color="#4d8fc0"/>
          <stop offset="1" stop-color="#1f72b8"/>
        </linearGradient>
      </defs>
      <path d="M40 0 L380 0 L380 700 L40 700 Q80 350 40 0 Z" fill="url(#poolTones)" role="img" aria-label="Photo of a swimmer in sparkling resort pool water"/>
      <path d="M0 0 L50 0 Q92 350 50 700 L0 700 Z" fill="var(--azure)"/>
      <path d="M0 0 L26 0 Q66 350 26 700 L0 700 Z" fill="var(--deep)"/>
      <path d="M0 0 L10 0 Q44 350 10 700 L0 700 Z" fill="var(--navy)"/>
      <path d="M50 700 Q200 640 380 660 L380 700 Z" fill="var(--deep)"/>
    </svg>
    <div class="cover-logo"><span class="mark"></span><span class="name">PBS</span></div>
    <span class="cover-logo-sub">Premier Basin Stewards</span>
    <h1 class="cover-title">Premier Basin<br>Stewards</h1>
    <p class="cover-slogan">Our slogan is "Sparkling Results"</p>
    <p class="cover-url">www.premier-basin-stewardsgrp.com</p>
  </section>

</main>
</body>
</html>
```